Brisbane IT support business needs our first website

Hi All,

We are after a new website design for our IT solutions and support business.The business name is Harlow Digital Systems Group, or HDSG for short. We provide a range of solutions and services within the IT space.

I would like to utilize the two colours in our business logo I have uploaded.

I understand this is initially for the design only aspect of the site, but I would like to engage the winner to finish coding the website and finalize after also.

Target Market(s)

Other businesses owners and home users.

Industry/Entity Type

Business

Requirements
Must have
• Nice clean and functional design utilizing our business colours from the logo.

```html
<!DOCTYPE html>
<html lang="en">
<head>
<meta charset="utf-8">
<title>Harlow Digital Systems Group</title>
<link rel="stylesheet" href="https://fonts.googleapis.com/css2?family=Open+Sans:wght@300;400;600;700;800&display=swap">
<style>
:root{
  --orange:#f07a1c;
  --orange-dark:#d9620e;
  --navy:#123a52;
  --ink:#333333;
  --muted:#8a8a8a;
  --dark:#1f1f1f;
  --darker:#161616;
  --light-bg:#e4ecef;
  --white:#ffffff;
}
*{box-sizing:border-box;margin:0;padding:0}
html,body{width:1200px;height:2876px;overflow:hidden}
body{position:relative;font-family:'Open Sans',Arial,sans-serif;color:var(--ink);background:var(--white)}
.abs{position:absolute}

/* header */
.site-header{left:0;top:0;width:1200px;height:73px;background:var(--white)}
.brand{left:162px;top:0;height:73px;display:flex;align-items:center}
.brand-name{font-size:19px;font-weight:600;color:var(--navy);white-space:nowrap}
.main-nav{left:520px;top:0;height:73px;display:flex}
.nav-item{width:86px;height:73px;display:flex;flex-direction:column;align-items:center;justify-content:center;gap:6px;font-size:11px;color:#666}
.nav-item svg{width:20px;height:20px}
.nav-item.active{background:var(--orange);color:var(--white)}

/* hero */
.hero{left:0;top:73px;width:1200px;height:489px;background:linear-gradient(120deg,#2b3540 0%,#55616c 40%,#8a8f93 70%,#c9c6c0 100%)}
.hero-shade{left:0;top:0;width:1200px;height:489px;background:rgba(0,0,0,.28)}
.hero-title{left:0;top:165px;width:1200px;text-align:center;font-size:46px;font-weight:800;color:var(--white);letter-spacing:2px}
.hero-sub{left:0;top:225px;width:1200px;text-align:center;font-size:16px;font-weight:600;line-height:20px;color:var(--white)}
.btn{display:flex;align-items:center;justify-content:center;gap:14px;background:var(--orange);color:var(--white);font-weight:700;letter-spacing:1px;border-radius:3px;box-shadow:0 3px 0 var(--orange-dark)}
.btn-arrow{width:22px;height:22px;border-radius:50%;background:#2a2a2a;display:flex;align-items:center;justify-content:center}
.hero-btn{left:478px;top:288px;width:246px;height:52px;font-size:19px}
.hero-arrow{top:220px;width:30px;height:50px}

/* services */
.services-title{left:0;top:585px;width:1200px;text-align:center;font-size:40px;font-weight:300;color:#444}
.services-title b{font-weight:600}
.services-sub{left:0;top:644px;width:1200px;text-align:center;font-size:14px;color:var(--muted)}
.service{top:697px;width:200px;text-align:center}
.service-icon{width:112px;height:112px;margin:0 auto;border-radius:50%;border:2px dashed var(--orange);display:flex;align-items:center;justify-content:center}
.service-icon .disc{width:96px;height:96px;border-radius:50%;background:var(--navy);display:flex;align-items:center;justify-content:center}
.service-icon.accent .disc{background:var(--orange)}
.service-name{margin-top:18px;font-size:16px;color:#444}
.service-text{margin-top:8px;font-size:11px;line-height:15px;color:var(--muted)}

/* feature bands */
.band-dark{left:0;top:936px;width:1200px;height:489px;background:linear-gradient(100deg,#121417 0%,#25292d 45%,#4a4a4a 75%,#2a2a2a 100%)}
.band-orange{left:0;top:1425px;width:1200px;height:614px;background:linear-gradient(100deg,#f7a462 0%,#f08a3a 45%,#ea741f 100%)}
.band-illustration{left:21px;top:1503px;width:528px;height:379px;border-radius:6px;background:linear-gradient(160deg,rgba(255,255,255,.35),rgba(30,120,140,.35))}
.feature-kicker{font-size:17px;font-weight:600;color:var(--white);white-space:nowrap}
.feature-head{font-size:24px;line-height:30px;color:var(--white);margin-top:8px;white-space:nowrap}
.feature-text{font-size:11px;line-height:16px;color:rgba(255,255,255,.85);margin-top:14px}
.feature-left{left:165px;top:1048px;width:560px}
.feature-right{left:460px;top:1605px;width:572px;text-align:right}

/* devices */
.band-light{left:0;top:2039px;width:1200px;height:661px;background:radial-gradient(ellipse at center,#ffffff 0%,var(--light-bg) 75%)}
.devices-title{left:0;top:2106px;width:1200px;text-align:center;font-size:23px;font-weight:600;color:#333}
.devices-text{left:180px;top:2148px;width:840px;text-align:center;font-size:13px;line-height:18px;color:var(--muted)}
.devices-art{left:374px;top:2222px;width:465px;height:288px;border-radius:8px;background:linear-gradient(180deg,#d8e6ee,#7fb6dc)}
.contact-btn{left:457px;top:2554px;width:249px;height:52px;font-size:18px}

/* footer */
.site-footer{left:0;top:2700px;width:1200px;height:134px;background:var(--dark)}
.social{top:24px;width:36px;height:36px;border-radius:50%;background:var(--white)}
.copyright{left:0;top:78px;width:1200px;text-align:center;font-size:10px;color:#bbb}
.legal{left:0;top:96px;width:1200px;text-align:center;font-size:10px;color:#bbb;word-spacing:2px}
.legal span{margin:0 10px}
.bottom-bar{left:0;top:2834px;width:1200px;height:42px;background:var(--darker);display:flex;justify-content:center;align-items:center;gap:34px;font-size:11px;color:#ccc}
</style>
</head>
<body>

<header class="site-header abs">
  <div class="brand abs"><span class="brand-name">Harlow Digital Systems Group</span></div>
  <nav class="main-nav abs">
    <div class="nav-item"><svg viewBox="0 0 20 20"><path d="M2 12 L10 4 L18 12" fill="none" stroke="#f07a1c" stroke-width="3"/></svg>Home</div>
    <div class="nav-item"><svg viewBox="0 0 20 20"><circle cx="10" cy="8" r="5" fill="none" stroke="#777" stroke-width="1.5"/><rect x="8" y="14" width="4" height="4" fill="#777"/></svg>How We Work</div>
    <div class="nav-item active"><svg viewBox="0 0 20 20"><circle cx="10" cy="10" r="8" fill="#fff"/><circle cx="10" cy="10" r="3" fill="#f07a1c"/></svg>Services</div>
    <div class="nav-item"><svg viewBox="0 0 20 20"><circle cx="10" cy="10" r="8" fill="none" stroke="#777" stroke-width="1.5"/><circle cx="10" cy="8" r="3" fill="#777"/></svg>About Us</div>
    <div class="nav-item"><svg viewBox="0 0 20 20"><rect x="4" y="6" width="12" height="8" fill="none" stroke="#777" stroke-width="1.5"/><path d="M4 6 L10 11 L16 6" fill="none" stroke="#777" stroke-width="1.5"/></svg>Contact</div>
    <div class="nav-item"><svg viewBox="0 0 20 20"><rect x="6" y="9" width="8" height="7" fill="#777"/><path d="M7.5 9 V6 a2.5 2.5 0 0 1 5 0 V9" fill="none" stroke="#777" stroke-width="1.5"/></svg>Login</div>
  </nav>
</header>

<section class="hero abs" role="img" aria-label="Photo of two businessmen in suits working together at a laptop">
  <div class="hero-shade abs"></div>
  <svg class="hero-arrow abs" style="left:55px" viewBox="0 0 30 50"><path d="M24 4 L6 25 L24 46" fill="none" stroke="#fff" stroke-width="3"/></svg>
  <svg class="hero-arrow abs" style="left:1085px" viewBox="0 0 30 50"><path d="M6 4 L24 25 L6 46" fill="none" stroke="#fff" stroke-width="3"/></svg>
  <h1 class="hero-title abs">WE MAKE YOUR DREAMS</h1>
  <p class="hero-sub abs">Lorem ipsum dolor sit amet, consectetuer adipiscing elit, sed diam nonummy<br>nibh euismod tincidunt ut laoreet.</p>
  <div class="btn hero-btn abs">LEARN MORE <span class="btn-arrow"><svg width="10" height="10" viewBox="0 0 10 10"><path d="M3 1 L7 5 L3 9" fill="none" stroke="#fff" stroke-width="2"/></svg></span></div>
</section>

<h2 class="services-title abs">Services We <b>Are Offering</b></h2>
<p class="services-sub abs">Duis autem vel eum iriure dolor in hendrerit in vulputate velit esse molestie consequat</p>

<div class="service abs" style="left:211px">
  <div class="service-icon accent"><div class="disc"><svg width="50" height="50" viewBox="0 0 50 50"><path d="M12 22 A14 14 0 0 1 36 14" fill="none" stroke="#fff" stroke-width="6"/><path d="M32 6 L42 16 L30 20 Z" fill="#fff"/><path d="M38 28 A14 14 0 0 1 14 36" fill="none" stroke="#fff" stroke-width="6"/><path d="M18 44 L8 34 L20 30 Z" fill="#fff"/></svg></div></div>
  <div class="service-name">Software Development</div>
  <p class="service-text">Lorem ipsum dolor sit amet,<br>consectetuer adipiscing elit, sed<br>tincidunt volutpat.</p>
</div>
<div class="service abs" style="left:405px">
  <div class="service-icon"><div class="disc"><svg width="54" height="40" viewBox="0 0 54 40"><path d="M14 34 a10 10 0 0 1 0-20 a14 14 0 0 1 26 -2 a11 11 0 0 1 2 22 Z" fill="#fff"/></svg></div></div>
  <div class="service-name">Application Designing</div>
  <p class="service-text">Lorem ipsum dolor sit amet,<br>consectetuer adipiscing elit, sed<br>tincidunt volutpat.</p>
</div>
<div class="service abs" style="left:600px">
  <div class="service-icon"><div class="disc"><svg width="52" height="46" viewBox="0 0 52 46"><rect x="3" y="3" width="46" height="30" fill="none" stroke="#fff" stroke-width="3"/><path d="M10 26 L20 16 L28 22 L42 9" fill="none" stroke="#fff" stroke-width="3"/><rect x="20" y="36" width="12" height="6" fill="#fff"/></svg></div></div>
  <div class="service-name">Internet Marketing</div>
  <p class="service-text">Lorem ipsum dolor sit amet,<br>consectetuer adipiscing elit, sed<br>tincidunt volutpat.</p>
</div>
<div class="service abs" style="left:794px">
  <div class="service-icon"><div class="disc"><svg width="52" height="46" viewBox="0 0 52 46"><rect x="3" y="3" width="46" height="30" fill="none" stroke="#fff" stroke-width="3"/><path d="M14 28 L36 8 L40 12 L18 30 Z" fill="#fff"/><rect x="20" y="36" width="12" height="6" fill="#fff"/></svg></div></div>
  <div class="service-name">Website Designing</div>
  <p class="service-text">Lorem ipsum dolor sit amet,<br>consectetuer adipiscing elit, sed<br>tincidunt volutpat.</p>
</div>

<section class="band-dark abs" role="img" aria-label="Photo of a businessman touching a glowing digital interface"></section>
<div class="feature-left abs">
  <div class="feature-kicker">Lorem ipsum dolor sit amet, consectetuer adipiscing</div>
  <div class="feature-head">Motivated team, excellent technical experters<br>Lorem Ipsum is simply dummy text of the</div>
  <p class="feature-text">Lorem ipsum dolor sit amet, consectetuer adipiscing elit, sed diam nonummy nibh euismod tincidunt ut laoreet dolore magna aliquam erat volutpat. Ut wisi enim ad minim veniam, quis nostrud exerci tation ullamcorper suscipit lobortis nisl ut aliquip ex ea commodo consequat.</p>
  <p class="feature-text">Duis autem vel eum iriure dolor in hendrerit in vulputate velit esse molestie consequat, vel illum dolore eu feugiat nulla facilisis at vero eros et accumsan et iusto odio dignissim qui blandit praesent luptatum.</p>
</div>

<section class="band-orange abs" role="img" aria-label="Orange background photo of a man in a suit"></section>
<div class="band-illustration abs" role="img" aria-label="Illustration of a desktop monitor with a world map, speech bubbles and a mobile phone"></div>
<div class="feature-right abs">
  <div class="feature-kicker">Web &amp; Mobile Product Development</div>
  <div class="feature-head">Motivated team, excellent technical experters<br>Lorem Ipsum is simply dummy text of the</div>
  <p class="feature-text">Lorem ipsum dolor sit amet, consectetuer adipiscing elit, sed diam nonummy nibh euismod tincidunt ut laoreet dolore magna aliquam erat volutpat. Ut wisi enim ad minim veniam, quis nostrud exerci tation ullamcorper suscipit lobortis nisl ut aliquip ex ea commodo consequat.</p>
  <p class="feature-text">Duis autem vel eum iriure dolor in hendrerit in vulputate velit esse molestie consequat, vel illum dolore eu feugiat nulla facilisis at vero eros et accumsan et iusto odio dignissim qui blandit praesent luptatum.</p>
</div>

<section class="band-light abs"></section>
<h2 class="devices-title abs">Lorem ipsum dolor sit amet, consectetuer adipiscing elit, sed diam nonummy</h2>
<p class="devices-text abs">Lorem ipsum dolor sit amet, consectetuer adipiscing elit, sed diam nonummy nibh euismod tincidunt ut laoreet dolore magna aliquam erat volutpat. Ut wisi enim ad minim veniam, quis nostrud exerci tation ullamcorper suscipit lobortis nisl ut aliquip ex ea commodo consequat.</p>
<div class="devices-art abs" role="img" aria-label="Illustration of a desktop, laptop, tablets and phone showing cloud screens"></div>
<div class="btn contact-btn abs">CONTACT US <span class="btn-arrow"><svg width="10" height="10" viewBox="0 0 10 10"><path d="M3 1 L7 5 L3 9" fill="none" stroke="#fff" stroke-width="2"/></svg></span></div>

<footer class="site-footer abs">
  <span class="social abs" style="left:536px"></span>
  <span class="social abs" style="left:581px"></span>
  <span class="social abs" style="left:625px"></span>
  <p class="copyright abs">Copyright © 2014 HDSG - All Rights Reserved.</p>
  <p class="legal abs"><span>Privacy Policy</span>|<span>Terms and Conditions</span>|<span>Acceptable Usage Policy</span></p>
</footer>
<nav class="bottom-bar abs"><span>Home</span><span>How We Work</span><span>Services</span><span>About Us</span><span>Contact</span><span>Login</span></nav>

</body>
</html>
```